Pellrow Strategies business card

I need a business card for my new strategic consulting LLC, Pellrow Strategies. We specialize in helping people who care about broadband technology and telecommunications policy, and we're based in Washington DC. I'm looking for a card that says smart, credible, future-facing and signals a high level of expertise. It's DC, so there's clearly a limit to how crazy we can go with this card, but I am looking for a design that reflects a company that is comfortable with technology, policy, and having a little bit fun. I'm uploading my logo below, and I'd like to have it be part of the card design in some fashion.
Target Market(s)
Telecommunications and technology policy professionals
Industry/Entity Type
Technology policy
Contact Information for Business Card
Name of business, my name (Colin Mabberly), email (colin@pellrowstrategies.example) , phone number (202-555-0148)phone number
Look and feel

```html
<!DOCTYPE html>
<html lang="en">
<head>
<meta charset="utf-8">
<title>Pellrow Strategies — Business Card</title>
<link href="https://fonts.googleapis.com/css2?family=Montserrat:wght@400;500;600;700&display=swap" rel="stylesheet">
<style>
  :root {
    --stage: #2b2b2d;
    --card-white: #fafafa;
    --brand-blue: #1550b3;
    --deep-blue: #0f4aa8;
    --sun-orange: #f5b335;
    --text-gray: #555555;
    --rule-gray: #9a9a9a;
  }
  * { margin: 0; padding: 0; box-sizing: border-box; }
  html, body {
    width: 1200px; height: 1200px; overflow: hidden;
    background: var(--stage);
    font-family: "Montserrat", sans-serif;
  }
  .stage {
    width: 1200px; height: 1200px;
    display: flex; flex-direction: column; align-items: center; justify-content: center;
    gap: 60px;
  }
  .card {
    width: 840px; height: 480px;
    position: relative;
    box-shadow: 0 14px 30px rgba(0,0,0,0.45);
  }
  .card-front { background: var(--card-white); }
  .card-back { background: var(--deep-blue); display: flex; align-items: center; justify-content: center; }

  .brand-name {
    position: absolute; left: 70px; top: 92px;
    display: flex; align-items: center; gap: 16px;
    font-weight: 700; font-size: 46px; color: var(--brand-blue);
    letter-spacing: -0.5px;
  }
  .brand-dot { width: 30px; height: 30px; border-radius: 50%; background: var(--sun-orange); flex: none; }

  .divider {
    position: absolute; left: 200px; right: 40px; top: 262px;
    height: 1px; background: var(--rule-gray);
  }
  .person {
    position: absolute; right: 40px; top: 176px; text-align: left;
  }
  .person-name { font-weight: 600; font-size: 34px; color: var(--brand-blue); line-height: 1.15; }
  .person-name .surname { color: var(--sun-orange); }
  .person-title { font-weight: 500; font-size: 20px; color: var(--text-gray); margin-top: 4px; letter-spacing: 0.4px; }

  .contact-list {
    position: absolute; left: 220px; top: 292px;
    list-style: none;
  }
  .contact-item {
    display: flex; align-items: center; gap: 14px;
    font-size: 21px; font-weight: 500; color: var(--text-gray);
    line-height: 1.75; letter-spacing: 0.3px;
  }
  .contact-icon { width: 20px; height: 20px; flex: none; }

  .back-brand {
    display: flex; align-items: center; gap: 20px;
    font-weight: 700; font-size: 52px; color: #ffffff;
  }
  .back-brand .brand-dot { width: 40px; height: 40px; }
</style>
</head>
<body>
<main class="stage">
  <section class="card card-front" aria-label="Business card front">
    <div class="brand-name"><span>Pellrow Strategies</span><span class="brand-dot"></span></div>

    <div class="person">
      <p class="person-name">Colin <span class="surname">Mabberly</span></p>
      <p class="person-title">Founder and President</p>
    </div>

    <div class="divider"></div>

    <ul class="contact-list">
      <li class="contact-item">
        <svg class="contact-icon" viewBox="0 0 24 24" aria-hidden="true"><path fill="var(--sun-orange)" d="M6.6 10.8c1.4 2.8 3.8 5.1 6.6 6.6l2.2-2.2c.3-.3.7-.4 1-.2 1.1.4 2.3.6 3.6.6.6 0 1 .4 1 1V20c0 .6-.4 1-1 1C10.6 21 3 13.4 3 4c0-.6.4-1 1-1h3.5c.6 0 1 .4 1 1 0 1.3.2 2.5.6 3.6.1.3 0 .7-.2 1z"/></svg>
        <span>202-555-0148</span>
      </li>
      <li class="contact-item">
        <svg class="contact-icon" viewBox="0 0 24 24" aria-hidden="true"><rect x="3" y="6" width="18" height="12" rx="1.5" fill="none" stroke="var(--sun-orange)" stroke-width="2"/><path d="M3.5 7l8.5 6 8.5-6" fill="none" stroke="var(--sun-orange)" stroke-width="2"/></svg>
        <span>colin@pellrowstrategies.example</span>
      </li>
      <li class="contact-item">
        <svg class="contact-icon" viewBox="0 0 24 24" aria-hidden="true"><g fill="none" stroke="var(--sun-orange)" stroke-width="1.8"><circle cx="12" cy="12" r="9"/><ellipse cx="12" cy="12" rx="4" ry="9"/><path d="M3 12h18M5 7.5h14M5 16.5h14"/></g></svg>
        <span>pellrowstrategies.example</span>
      </li>
    </ul>
  </section>

  <section class="card card-back" aria-label="Business card back">
    <div class="back-brand"><span class="brand-dot"></span><span>Pellrow Strategies</span></div>
  </section>
</main>
</body>
</html>
```